Emergency Vehicle Installer and Security Firm Needs a Business Card

Our company "Corvalta" need a business card for our Emergency Vehicle Equipment Installation and Infrastructure Security Business. We are contract designers, manufacturers and installers for Emergency Vehicle Fleets. This includes installation of Emergency Lights, Sirens, Vehicle Graphics and Radio Communications. We also supply this products to an international market. We also do consultant, and installation of high level security access, alarm and surveillance equipment for medium to large size businesses.

The design should represent a level of trust in our professionalism and expertise. It should visually display our ongoing relationship with the emergency services, but not overtake our commitment to high level security options.

Target Market(s)

Emergency Services and Businesses requiring high level security

Industry/Entity Type

Business

Contact Information for Business Card

*note complete details will be given to the winning designer for revising. The name "Mark Pelling will be used to fill in name".

Mark Pelling
Managing Director
Corvalta NZ Limited
Phone: +64 027 846 20193
Email: mark.pelling@corvalta-example.co.nz

Requirements
Must have
• Card must be in black. Using our logo on the top as supplied. Designers should try having the reverse side as a blurred image of police lights (red and blue) with our logo in greyscale in the centre (this is not particularly a requirement, but feel free to play around with this option).
Nice to have
• A card design that looks good when spot UV printed. A clean compact and graphic design. A grey scale feel on the front (excluding logo, but you can play around with that idea). Rounded smooth text.
Should not have
• Will update this section as designs come through - feel free to submit what you feel would look good.

```html
<!DOCTYPE html>
<html lang="en">
<head>
<meta charset="utf-8">
<title>Corvalta Business Card</title>
<link href="https://fonts.googleapis.com/css2?family=Montserrat:wght@800&family=Lato:wght@400;700;900&display=swap" rel="stylesheet">
<style>
  :root {
    --canvas: #d9d9d9;
    --card-black: #050505;
    --card-white: #ffffff;
    --ink: #1a1a1a;
    --accent-red: #e8202a;
    --rule: #444444;
  }
  * { margin: 0; padding: 0; box-sizing: border-box; }
  html, body { width: 1200px; height: 1200px; overflow: hidden; }
  body {
    background: var(--canvas);
    font-family: "Lato", sans-serif;
    position: relative;
  }
  .card {
    position: absolute;
    left: 250px;
    width: 700px;
    height: 400px;
    overflow: hidden;
    box-shadow: 0 10px 30px rgba(0,0,0,0.25);
  }
  .card--back { top: 110px; background: var(--card-black); }
  .card--front { top: 640px; background: var(--card-white); }

  .wordmark {
    font-family: "Montserrat", sans-serif;
    font-weight: 800;
    letter-spacing: 2px;
    line-height: 1;
  }
  .card--back .wordmark {
    position: absolute;
    top: 150px;
    left: 0; right: 0;
    text-align: center;
    font-size: 78px;
    color: var(--card-white);
  }
  .card--back .site {
    position: absolute;
    top: 265px;
    left: 0; right: 0;
    text-align: center;
    font-size: 15px;
    color: var(--card-white);
    letter-spacing: 0.5px;
  }

  .card--front .brand {
    position: absolute;
    left: 55px;
    top: 160px;
    display: flex;
    align-items: center;
    gap: 12px;
  }
  .card--front .wordmark { font-size: 46px; color: var(--ink); }
  .brand-dot { width: 14px; height: 14px; background: var(--accent-red); }

  .divider {
    position: absolute;
    left: 395px;
    top: 40px;
    width: 1.5px;
    height: 190px;
    background: var(--rule);
  }
  .contact {
    position: absolute;
    left: 420px;
    top: 40px;
    color: var(--ink);
    font-size: 15px;
    line-height: 1.5;
  }
  .contact .name { font-size: 22px; font-weight: 900; margin-bottom: 2px; }
  .contact .name .surname { color: var(--accent-red); }
  .contact .line { display: flex; align-items: center; gap: 9px; }
  .contact .icons { margin-top: 6px; }
  .contact svg { width: 14px; height: 14px; flex: none; }

  .base-band { position: absolute; left: 0; bottom: 0; width: 700px; height: 60px; }
</style>
</head>
<body>
  <section class="card card--back" aria-label="Card back">
    <div class="wordmark">CORVALTA</div>
    <div class="site">www.corvalta-example.co.nz</div>
  </section>

  <section class="card card--front" aria-label="Card front">
    <div class="brand">
      <div class="wordmark">CORVALTA</div>
      <span class="brand-dot"></span>
    </div>

    <div class="divider"></div>

    <div class="contact">
      <div class="name">Mark <span class="surname">Pelling</span></div>
      <div>Managing Director</div>
      <div>2208 Harbour Rd</div>
      <div>Wellington, nz 60142</div>
      <div class="icons">
        <div class="line">
          <svg viewBox="0 0 24 24"><path fill="var(--accent-red)" d="M6.6 10.8a15.1 15.1 0 0 0 6.6 6.6l2.2-2.2a1 1 0 0 1 1-.25 11.4 11.4 0 0 0 3.6.57 1 1 0 0 1 1 1V20a1 1 0 0 1-1 1A17 17 0 0 1 3 4a1 1 0 0 1 1-1h3.5a1 1 0 0 1 1 1c0 1.25.2 2.45.57 3.57a1 1 0 0 1-.25 1z"/></svg>
          <span>+64 027 846 20193</span>
        </div>
        <div class="line">
          <svg viewBox="0 0 24 24"><path fill="var(--accent-red)" d="M2 5h20v14H2z"/><path fill="none" stroke="#fff" stroke-width="2" d="M2 5l10 8 10-8"/></svg>
          <span>mark.pelling@corvalta-example.co.nz</span>
        </div>
        <div class="line">
          <svg viewBox="0 0 24 24"><g fill="none" stroke="var(--accent-red)" stroke-width="2"><circle cx="12" cy="12" r="10"/><ellipse cx="12" cy="12" rx="4" ry="10"/><path d="M2 12h20"/></g></svg>
          <span>www.corvalta-example.co.nz</span>
        </div>
      </div>
    </div>

    <svg class="base-band" viewBox="0 0 700 60" aria-hidden="true">
      <polygon points="0,42 560,42 585,12 700,12 700,60 0,60" fill="var(--accent-red)"/>
      <polygon points="572,60 610,12 700,12 700,60" fill="var(--card-black)"/>
      <polygon points="560,42 585,12 598,12 573,42" fill="var(--card-white)"/>
    </svg>
  </section>
</body>
</html>
```